Company raising consciousness thru leadership & self-awareness needs amazing Letterhead

We are a technology company that spun out of a consulting firm. We are waking people up in corporate America through surveys, leadership development, workshops and consulting. Getting employees to become self-aware and changing company culture through improved leadership and team effectiveness. We need Word letterhead for our proposals, handouts, and worksheets that match our brand standard, is fresh, and communicates trust, credibility and professionalism.

Target Market(s)

Our target clients are other businesses, and executive leaders and C-suite leaders in those companies.

Font styles to use
Sans Serif

Requirements
Must have
• A Word template we can use for handouts, proposals, executive summary, project management documents, and letters. We need our logo. Please add page number and date on the footer. Must match the theme of our new website in look and feel to match the brand we are trying to promote. Use the colors from our brand standard document I submitted.

```html
<!DOCTYPE html>
<html lang="en">
<head>
<meta charset="utf-8">
<title>Veloris Letterhead</title>
<link href="https://fonts.googleapis.com/css2?family=Open+Sans:wght@400;600&family=Roboto:wght@400&family=Montserrat:wght@600&display=swap" rel="stylesheet">
<style>
  :root {
    --backdrop: #ececed;
    --paper: #ffffff;
    --navy: #44598c;
    --sky: #4bb5e3;
    --ink: #6e6e72;
    --ink-dark: #4a4a50;
    --brand: #3f5a92;
  }
  * { margin: 0; padding: 0; box-sizing: border-box; }
  html, body {
    width: 1200px; height: 795px; overflow: hidden;
    background: var(--backdrop);
  }
  .letterhead {
    position: absolute; left: 330px; top: 16px;
    width: 540px; height: 763px;
    background: var(--paper);
    box-shadow: 0 2px 10px rgba(0,0,0,0.10);
    font-family: "Open Sans", sans-serif;
    color: var(--ink);
    overflow: hidden;
  }
  .brand {
    position: absolute; left: 48px; top: 62px;
    display: flex; align-items: center; gap: 8px;
  }
  .brand-dot {
    width: 22px; height: 22px; border-radius: 50%;
    background: var(--brand);
  }
  .brand-name {
    font-family: "Montserrat", sans-serif; font-weight: 600;
    font-size: 24px; letter-spacing: 1px; color: var(--brand);
  }
  .contact {
    position: absolute; right: 48px; top: 52px;
    padding-left: 14px;
    border-left: 1.5px solid var(--sky);
    font-family: "Roboto", sans-serif; font-size: 10.5px;
    color: var(--ink-dark); line-height: 16px;
  }
  .contact li { list-style: none; display: flex; align-items: center; gap: 6px; }
  .contact svg { width: 10px; height: 10px; fill: var(--navy); }
  .letter-body {
    position: absolute; left: 58px; top: 150px; width: 420px;
    font-size: 10px; line-height: 15.5px;
  }
  .salutation { margin-bottom: 14px; }
  .letter-body p.para { margin-bottom: 15px; }
  .closing { margin-top: 16px; }
  .signature-area {
    margin-top: 10px; width: 110px; height: 56px;
    background: linear-gradient(135deg, #f2f2f3, #e6e6e8);
    border-radius: 4px;
  }
  .address {
    position: absolute; left: 240px; bottom: 40px;
    display: flex; align-items: center; gap: 6px;
    font-family: "Roboto", sans-serif; font-size: 11.5px; color: var(--ink-dark);
  }
  .address svg { width: 10px; height: 13px; fill: var(--navy); }
  .footer-band {
    position: absolute; left: 0; bottom: 0; width: 540px; height: 10px;
  }
</style>
</head>
<body>
  <main class="letterhead">
    <header>
      <div class="brand">
        <span class="brand-dot"></span>
        <span class="brand-name">VELORIS</span>
      </div>
      <ul class="contact">
        <li><svg viewBox="0 0 10 10"><path d="M2 0.5 L4 2.5 L3 3.8 Q4.5 6 6.2 7 L7.5 6 L9.5 8 L8 9.5 Q3 9 0.5 2 Z"/></svg>555-210-4400</li>
        <li><svg viewBox="0 0 10 10"><rect x="0.5" y="3" width="9" height="6" rx="1"/><rect x="2" y="1" width="6" height="2"/></svg>555-210-4401</li>
        <li><svg viewBox="0 0 10 10"><path d="M0.5 2 H9.5 V8.5 H0.5 Z M0.5 2 L5 5.5 L9.5 2" stroke="#fff" stroke-width="0.8"/></svg>hello@veloris-mail.com</li>
        <li><svg viewBox="0 0 10 10"><circle cx="5" cy="5" r="4.5"/></svg>www.veloris-web.com</li>
      </ul>
    </header>

    <section class="letter-body">
      <p class="salutation">Dear customer,</p>
      <p class="para">Lorem ipsum dolor sit amet, consectetur adipisicing elit, sed do eiusmod tempor incididunt ut labore et dolore magna aliqua. Ut enim ad minim veniam, quis nostrud exercitation ullamco laboris nisi ut aliquip ex ea commodo consequat. Duis aute irure dolor in reprehenderit in voluptate velit esse cillum dolore eu fugiat nulla pariatur. Excepteur sint occaecat cupidatat non proident, sunt in culpa qui officia deserunt mollit anim id est laborum.</p>
      <p class="para">Lorem ipsum dolor sit amet, consectetur adipisicing elit, sed do eiusmod tempor incididunt ut labore et dolore magna aliqua. Ut enim ad minim veniam, quis nostrud exercitation ullamco laboris nisi ut aliquip ex ea commodo consequat. Duis aute irure dolor in reprehenderit in voluptate velit esse cillum dolore eu fugiat nulla pariatur. Excepteur sint occaecat cupidatat non proident, sunt in culpa qui officia deserunt mollit anim id est laborum.</p>
      <p class="para">Lorem ipsum dolor sit amet, consectetur adipisicing elit, sed do eiusmod tempor incididunt ut labore et dolore magna aliqua. Ut enim ad minim veniam, quis nostrud exercitation ullamco laboris nisi ut aliquip ex ea commodo consequat. Duis aute irure dolor in reprehenderit in voluptate velit esse cillum dolore eu fugiat nulla pariatur. Excepteur sint occaecat cupidatat non proident, sunt in culpa qui officia deserunt mollit anim id est laborum.</p>
      <p class="para">Lorem ipsum dolor sit amet, consectetur adipisicing elit, sed do eiusmod tempor incididunt ut labore et dolore magna aliqua. Ut enim ad minim veniam, quis nostrud exercitation ullamco laboris nisi ut aliquip ex ea commodo consequat. Duis aute irure dolor in reprehenderit.</p>
      <p class="closing">Yours Sincerely,</p>
      <div class="signature-area" role="img" aria-label="Handwritten signature of the sender"></div>
    </section>

    <footer>
      <div class="address">
        <svg viewBox="0 0 10 13"><path d="M5 0 A5 5 0 0 1 10 5 C10 8 5 13 5 13 C5 13 0 8 0 5 A5 5 0 0 1 5 0 Z M5 3 A2 2 0 1 0 5.01 3 Z"/></svg>
        48 Harbor Lane, Suite 310, Ashford, NY 10502
      </div>
      <svg class="footer-band" viewBox="0 0 540 10" preserveAspectRatio="none">
        <polygon points="0,0 330,0 320,10 0,10" fill="var(--navy)"/>
        <polygon points="333,0 540,0 540,10 323,10" fill="var(--sky)"/>
      </svg>
    </footer>
  </main>
</body>
</html>
```